Corrigan Construction Law P.A.

Business Card with Corporate Logo. For a law firm specializing in construction law.

need address, telephone, email and website. Also, have an elegant and conservative logo.

Logo so it is RBN.

Full name "Gordon T. Corrigan

Under my name title "Attorney at Law"

Under title "Board Certified in Construction Law"

PA in email is lower case

Add logo to back side of card

Mix in a bit of gold color into card to go with the green

Some color on bottom
Updates

Target Market(s)

legal

Industry/Entity Type

Construction

Contact Information for Business Card

I like it -- edits: 1. add "L" to logo so it is RBN. 2. add my full name "Gordon T. Business Card with Corporate Logo. For a law firm specializing in construction law.

Logo so it is RBN.

PA in email is lower case

Font styles to use
Serif

Colors
00a990
f78f20

Requirements
Must have
• Conservative legal designed logo for construction market
• Address:
• Corrigan Construction Law, P.A.
• 4150 Meadowlark Ave North, Ste B4
• Jacksonville, Florida 32217
• Main: 904-555-3172
• Direct: 904-555-8410
• Fax: 904-555-8410
• gt@corriganpa-example.com
• www.corriganbuildlaw-example.com
Nice to have
• Catchy conservative logo on card
Should not have
• Flashy

```html
<!DOCTYPE html>
<html lang="en">
<head>
<meta charset="utf-8">
<title>Corrigan Construction Law – Business Card</title>
<link href="https://fonts.googleapis.com/css2?family=Libre+Baskerville:wght@400;700&display=swap" rel="stylesheet">
<style>
  :root {
    --page-bg: #d9dbde;
    --card-white: #ffffff;
    --panel-grey: #eef0ef;
    --brand-green: #00a990;
    --brand-green-light: #5fd3bf;
    --brand-gold: #f78f20;
    --ink-dark: #2b2e33;
    --ink-mid: #4a4f56;
  }
  * { margin: 0; padding: 0; box-sizing: border-box; }
  html, body {
    width: 1200px; height: 988px; overflow: hidden;
    background: var(--page-bg);
    font-family: "Libre Baskerville", Georgia, serif;
  }
  .sheet {
    width: 1200px; height: 988px;
    display: flex; flex-direction: column; align-items: center; justify-content: center;
    gap: 32px;
  }
  .card {
    position: relative;
    width: 780px; height: 446px;
    background: var(--card-white);
    box-shadow: 0 6px 18px rgba(0,0,0,0.18);
    overflow: hidden;
  }

  /* Logo block (shared) */
  .logo { text-align: center; color: var(--brand-green); font-weight: 400; }
  .logo__initials { font-size: 62px; letter-spacing: 8px; line-height: 1; }
  .logo__name { font-size: 12px; letter-spacing: 2px; text-transform: uppercase; margin-top: 8px; }

  /* Back side */
  .card--back .band {
    position: absolute; left: 0; right: 0; height: 96px;
    background: linear-gradient(90deg, var(--brand-green) 0%, var(--brand-green-light) 35%, var(--brand-green) 100%);
  }
  .card--back .band--top { top: 34px; border-bottom: 4px solid var(--brand-gold); }
  .card--back .band--bottom { bottom: 34px; border-top: 4px solid var(--brand-gold); }
  .card--back .logo {
    position: absolute; left: 0; right: 0; top: 50%; transform: translateY(-50%);
  }

  /* Front side */
  .card--front .panel {
    position: absolute; left: 0; right: 0; top: 0; height: 252px;
    background: var(--panel-grey);
  }
  .card--front .logo { position: absolute; left: 0; right: 0; top: 30px; }
  .card--front .logo__initials { font-size: 54px; }
  .person { position: absolute; left: 0; right: 0; top: 146px; text-align: center; }
  .person__name { font-size: 21px; font-weight: 700; letter-spacing: 3px; color: var(--ink-dark); }
  .person__title { font-size: 13px; letter-spacing: 2px; color: var(--brand-gold); margin-top: 8px; }
  .person__cert { font-size: 11px; letter-spacing: 1px; color: var(--ink-mid); margin-top: 6px; }

  .contacts {
    position: absolute; left: 120px; top: 272px;
    display: grid; grid-template-columns: 230px 330px; row-gap: 10px; column-gap: 30px;
    font-size: 12px; line-height: 17px; color: var(--ink-dark);
  }
  .contact { display: flex; align-items: center; gap: 9px; white-space: nowrap; }
  .contact--wide { grid-column: 1 / span 2; }
  .contact__label { color: var(--brand-green); font-weight: 700; }
  .contact svg { width: 16px; height: 16px; flex: none; }

  .rule-thick {
    position: absolute; left: 40px; right: 40px; bottom: 36px; height: 4px;
    background: var(--brand-gold);
  }
  .rule-base {
    position: absolute; left: 0; right: 0; bottom: 0; height: 16px;
    background: var(--brand-green);
  }
</style>
</head>
<body>
<main class="sheet">

  <section class="card card--back" aria-label="Card back">
    <div class="band band--top"></div>
    <div class="logo">
      <div class="logo__initials">RBN</div>
      <div class="logo__name">Corrigan Construction Law, P.A.</div>
    </div>
    <div class="band band--bottom"></div>
  </section>

  <section class="card card--front" aria-label="Card front">
    <div class="panel"></div>
    <div class="logo">
      <div class="logo__initials">RBN</div>
      <div class="logo__name">Corrigan Construction Law, P.A.</div>
    </div>
    <div class="person">
      <div class="person__name">GORDON T. CORRIGAN</div>
      <div class="person__title">ATTORNEY AT LAW</div>
      <div class="person__cert">Board Certified in Construction Law</div>
    </div>

    <div class="contacts">
      <div class="contact">
        <svg viewBox="0 0 16 16"><circle cx="8" cy="8" r="8" fill="#00a990"/><path d="M5.3 4.2l1.4 1.6-.7 1a5 5 0 0 0 2.6 2.6l1-.7 1.6 1.4-.8 1.2c-3 0-5.9-2.9-5.9-5.9z" fill="#fff"/></svg>
        <span><span class="contact__label">Main:</span> 904-555-3172</span>
      </div>
      <div class="contact">
        <svg viewBox="0 0 16 16"><circle cx="8" cy="8" r="8" fill="#00a990"/><path d="M5.3 4.2l1.4 1.6-.7 1a5 5 0 0 0 2.6 2.6l1-.7 1.6 1.4-.8 1.2c-3 0-5.9-2.9-5.9-5.9z" fill="#fff"/></svg>
        <span><span class="contact__label">Direct:</span> 904-555-8410</span>
      </div>
      <div class="contact">
        <svg viewBox="0 0 16 16"><circle cx="8" cy="8" r="8" fill="#00a990"/><rect x="4.5" y="6" width="7" height="4.5" fill="#fff"/><rect x="5.5" y="3.5" width="5" height="2.5" fill="none" stroke="#fff" stroke-width="0.9"/></svg>
        <span><span class="contact__label">Fax:</span> 904-555-8410</span>
      </div>
      <div class="contact">
        <svg viewBox="0 0 16 16"><circle cx="8" cy="8" r="8" fill="#00a990"/><rect x="4" y="5" width="8" height="6" fill="none" stroke="#fff" stroke-width="1"/><path d="M4 5l4 3.2L12 5" fill="none" stroke="#fff" stroke-width="1"/></svg>
        <span>gt@corriganpa-example.com</span>
      </div>
      <div class="contact contact--wide">
        <svg viewBox="0 0 16 16"><circle cx="8" cy="8" r="8" fill="#00a990"/><circle cx="8" cy="8" r="4" fill="none" stroke="#fff" stroke-width="1"/><path d="M4 8h8M8 4c-2 2.4-2 5.6 0 8M8 4c2 2.4 2 5.6 0 8" fill="none" stroke="#fff" stroke-width="0.8"/></svg>
        <span>www.corriganbuildlaw-example.com</span>
      </div>
      <div class="contact contact--wide">
        <svg viewBox="0 0 16 16"><circle cx="8" cy="8" r="8" fill="#00a990"/><path d="M8 3.5a3 3 0 0 1 3 3c0 2.2-3 6-3 6s-3-3.8-3-6a3 3 0 0 1 3-3z" fill="#fff"/><circle cx="8" cy="6.5" r="1.1" fill="#00a990"/></svg>
        <span>4150 Meadowlark Ave North, Ste B4, Jacksonville, Florida 32217</span>
      </div>
    </div>

    <div class="rule-thick"></div>
    <div class="rule-base"></div>
  </section>

</main>
</body>
</html>
```